The Cedarline Newsletter For My Monthly Investment Newsletters

I'm looking to create two beautiful newsletter template for my new financial planning and investment firm. I keep my newsletters short and sweet as I feel less is more. One newsletter is for investment updates - I send that to clients and prospects. The other is more of an update for clients only.

I'm going to be using Mailchimp & Constant Contact so please make sure I can use that template there.

My newsletter typically goes out monthly. There are two versions - one for clients and one for prospects. Sometimes, information is applicable for clients only.

The newsletter brief should have the month and year in it like
The Cedarline Newsletter: March 2020.

The other can be

The Cedarline Update: March 2020 (for more administrative announcements).

Target Market(s)

Investors

Industry/Entity Type

Investment Advisory

Font styles to use
Sans Serif

Colors

Designer to choose colors to be used in the design.

Requirements
Must have
• Clean
• professional
• Modern feel
• Less is more.
• Colors should match and be in sync my logo.
• I'm going to be using Mailchimp & Constant Contact so please make sure I can use that template there.
Nice to have
• Please follow the must haves

```html
<!DOCTYPE html>
<html lang="en">
<head>
<meta charset="utf-8">
<title>The Cedarline Newsletter: March 2020</title>
<link href="https://fonts.googleapis.com/css2?family=Montserrat:ital,wght@0,400;0,500;0,600;0,700;1,700&display=swap" rel="stylesheet">
<style>
:root{
  --orange:#e8850f;
  --cyan:#1fb3d9;
  --ink:#2b2b2b;
  --dark:#1f1f1f;
  --hero:#2a2d33;
  --paper:#ffffff;
  --mist:#ececec;
  --link:#d4222a;
}
*{margin:0;padding:0;box-sizing:border-box}
html,body{width:1200px;height:3304px;overflow:hidden;background:var(--paper)}
body{position:relative;font-family:'Montserrat',sans-serif;color:var(--ink)}
.abs{position:absolute}
.topbar{left:0;top:0;width:1200px;height:66px;background:var(--orange);color:#fff}
.topbar .brand{left:88px;top:16px;font-size:26px;font-weight:700;font-style:italic}
.topbar .browser{right:110px;top:16px;font-size:25px;font-style:italic;font-weight:500;text-decoration:underline;display:flex;align-items:center;gap:14px}
.hero{left:0;top:66px;width:1200px;height:548px;background:linear-gradient(120deg,#23262b 0%,#3a3d43 45%,#4a4d52 70%,#2c2f34 100%)}
.hero-logo{left:0;width:1200px;top:100px;display:flex;justify-content:center;align-items:center;gap:18px;color:#fff;font-size:46px;font-weight:600}
.hero-logo .dot{width:52px;height:52px;border-radius:50%;background:#fff}
.hero-title{left:0;width:1200px;top:226px;text-align:center;color:#fff;font-size:54px;font-weight:500;letter-spacing:3px}
.hero-sub{left:0;width:1200px;top:308px;text-align:center;color:#fff;font-size:26px;line-height:32px;font-weight:400;letter-spacing:.5px}
.btn{display:flex;align-items:center;justify-content:center;width:224px;height:62px;border-radius:31px;background:var(--cyan);color:#fff;font-size:27px;font-weight:700;letter-spacing:1px}
.hero .btn{position:absolute;left:488px;top:410px}
.update{left:60px;width:1080px;height:322px;background:#fff;box-shadow:0 2px 8px rgba(0,0,0,.18)}
.update .thumb{position:absolute;left:0;top:0;width:292px;height:322px}
.update h2{position:absolute;left:316px;top:14px;font-size:30px;font-weight:500;color:var(--orange);letter-spacing:.5px}
.update p{position:absolute;left:344px;top:62px;width:700px;font-size:25px;line-height:31px}
.feature{top:1484px;width:508px;height:796px;background:#fff;box-shadow:0 2px 8px rgba(0,0,0,.15);z-index:2}
.feature .thumb{position:absolute;left:0;top:0;width:508px;height:316px}
.feature h3{position:absolute;left:0;top:316px;width:508px;height:74px;background:var(--orange);color:#fff;font-size:31px;font-weight:600;display:flex;align-items:center;justify-content:center;letter-spacing:1px}
.feature p{position:absolute;left:44px;top:428px;width:420px;text-align:center;font-size:25px;line-height:31.5px}
.feature .btn{position:absolute;left:136px;top:684px}
.stable-bg{left:0;top:2196px;width:1200px;height:600px;background:linear-gradient(100deg,#2a2622 0%,#4b4038 40%,#3a322c 70%,#221e1b 100%)}
.stable{left:60px;top:2342px;width:1080px;height:370px}
.stable h3{height:74px;background:var(--orange);color:#fff;font-size:31px;font-weight:600;display:flex;align-items:center;justify-content:center;letter-spacing:1px}
.stable .body{height:296px;background:rgba(240,240,240,.9);position:relative}
.stable p{position:absolute;left:80px;top:26px;width:920px;text-align:center;font-size:25px;line-height:31px}
.stable .btn{position:absolute;left:428px;top:184px}
.social{left:0;top:2838px;width:1200px;height:104px;background:var(--orange);color:#fff}
.social .label{left:86px;top:38px;font-size:26px;font-weight:600;letter-spacing:2px}
.social .icons{right:116px;top:36px;display:flex;gap:42px}
.social .icons span{width:34px;height:34px;border-radius:7px;background:#fff}
.footer{left:0;top:2942px;width:1200px;height:270px;background:var(--dark);color:#fff}
.footer .tower{position:absolute;left:0;top:40px;width:460px;height:230px;background:linear-gradient(135deg,#1f1f1f 10%,#8a8a8a 55%,#d8d8d8 70%,#3a3a3a 100%)}
.footer .address{position:absolute;left:500px;top:54px;width:680px;text-align:center;font-size:26px;line-height:33px}
.footer .contact{position:absolute;left:528px;top:144px;font-size:26px;display:flex;gap:54px}
.legal{left:0;top:3212px;width:1200px;height:92px;background:var(--mist);text-align:center;font-size:24px;line-height:29px;padding-top:16px;color:#333}
.legal a{color:var(--link);text-decoration:underline}
</style>
</head>
<body>

<header class="abs topbar">
  <div class="abs brand">The Cedarline LLC</div>
  <div class="abs browser">
    <svg width="26" height="22" viewBox="0 0 26 22" aria-hidden="true"><rect x="1.5" y="1.5" width="23" height="14" rx="1.5" fill="none" stroke="#fff" stroke-width="3"/><rect x="9" y="17" width="8" height="3" fill="#fff"/></svg>
    View on browser
  </div>
</header>

<section class="abs hero" role="img" aria-label="Hands reviewing financial documents with a pen, darkened background photo">
  <div class="abs hero-logo" style="top:34px"><span class="dot"></span>The Cedarline LLC</div>
  <h1 class="abs hero-title">The Cedarline: March 2020</h1>
  <p class="abs hero-sub">It shows investors with the latest information on the<br>performance and portfolio composition of our products.</p>
  <a class="btn">Read More</a>
</section>

<article class="abs update" style="top:716px">
  <div class="thumb" role="img" aria-label="Financial calculator on printed statements" style="background:linear-gradient(135deg,#e6e6e6 0%,#bdbdbd 40%,#2a2a2a 60%,#8c8c8c 100%)"></div>
  <h2>INVESTMENT UPDATE 1</h2>
  <p>Orci varius natoque penatibus et magnis dis parturient montes, nascetur ridiculus mus. Cras feugiat lorem in nisl imperdiet dapibus sit amet at urna. Morbi egestas eros vel dolor accumsan congue. Orci varius natoque penatibus et magnis dis parturient montes, nascetur ridiculus mus. Quisque ut nulla finibus ipsum hendrerit cursus.</p>
</article>

<article class="abs update" style="top:1088px">
  <div class="thumb" role="img" aria-label="Tablet showing charts beside printed reports on a wooden desk" style="background:linear-gradient(160deg,#8a5a3a 0%,#d9d4cf 45%,#3c3c3c 70%,#c9c2bb 100%)"></div>
  <h2>INVESTMENT UPDATE 2</h2>
  <p>Cras vehicula, arcu et rutrum posuere, ipsum nisl dignissim ipsum, vitae bibendum erat nisl et arcu. Nullam eu felis quis urna volutpat venenatis. Nunc et felis id magna pulvinar pharetra. Aenean mattis libero nec aliquam consectetur.</p>
</article>

<div class="abs stable-bg" role="img" aria-label="Team meeting around a table, darkened background photo"></div>

<article class="abs feature" style="left:60px">
  <div class="thumb" role="img" aria-label="Colleagues in a casual office discussion" style="background:linear-gradient(160deg,#dfe3e6 0%,#9aa3ab 45%,#5a5f66 75%,#b9b2a8 100%)"></div>
  <h3>DISTRIBUTIONS</h3>
  <p>Morbi finibus velit ligula, eget ornare ipsum pellentesque ac. Cras vehicula, arcu et rutrum posuere, ipsum nisl dignissim ipsum, vitae bibendum erat nisl et arcu. Nullam eu felis quis urna volutpat venenatis.</p>
  <a class="btn">Read More</a>
</article>

<article class="abs feature" style="left:632px">
  <div class="thumb" role="img" aria-label="Business handshake over a boardroom table" style="background:linear-gradient(150deg,#3d3d3d 0%,#8e7a66 40%,#c8ad95 60%,#4a4a4a 100%)"></div>
  <h3>NEW INVESTMENT PLANS</h3>
  <p>Vestibulum rutrum leo erat, ut condimentum sem ullamcorper id. Praesent ut feugiat elit. Maecenas malesuada massa in nunc finibus, id semper felis eleifend. Fusce elementum lobortis erat sed dictum.</p>
  <a class="btn">Read More</a>
</article>

<section class="abs stable">
  <h3>BE FINANCIALLY STABLE</h3>
  <div class="body">
    <p>Morbi egestas eros vel dolor accumsan congue. Quisque ut nulla finibus ipsum hendrerit cursus. Sed scelerisque, nibh nec efficitur tincidunt, lorem mi molestie justo, eget facilisis lacus nisi a diam. Curabitur sit amet condimentum nunc.</p>
    <a class="btn">Read More</a>
  </div>
</section>

<section class="abs social">
  <div class="abs label">FOLLOW US ONLINE</div>
  <div class="abs icons" aria-label="Social links"><span></span><span></span><span></span><span></span><span></span><span></span></div>
</section>

<footer class="abs footer">
  <div class="tower" role="img" aria-label="Black and white modern office tower"></div>
  <p class="address">Unit 5, Harbour Court, Maple Street<br>Riverside, Port Ellan,</p>
  <div class="contact"><span>www.thecedarline.com</span><span>Phone: 000 000 0000</span></div>
</footer>

<div class="abs legal">You are receiving this email because you have subscribe to receive updates from us.<br>Should you wish to cancel your subscription , please <a>click here to unsubscribe.</a></div>

</body>
</html>
```